Transfer Falcon - Cloud Based Data Migration Service for IT Professionals

We are looking for a smart clean website design for an informational site about our services and as a main portal into the service itself. We would like the design completed in WORDPRESS so that it will easily connect with the service.

Transfer Falcon is a cloud based migration service providing (to start with) a online migration tool that we migrate Quillnet Relay mailboxes (email) with all the settings, attachments from one system to another.
The service is aimed at IT professionals, IT companies and IT departments so our customers will be very technology based.

The Service -
IT companies currently migrate email; data and databases. using a very time intensive process which is both expensive and means their customer potentially losses access to its IT for a significant period of time. Additionally there are risks with regards to compatibility between systems and loss of data.
Potential benefits include;
• cost savings
• improved customer service, including reduced downtime
• improved resilience of the process
We are therefore developing cloud based migration software/website which will automate the process, mitigating these issues, as well as providing additional benefits such as the ability to sort and migrate only certain areas of data or certain emails, to check the integrity of the data/emails moved and to also repair corrupted data and emails.
The system will effectively duplicate the data and emails onto the new system over the weeks prior to the completion date. This will enable the IT Company to complete a final synchronisation and then immediately switch over to the new system with no interruption to the end users.
There is also an added benefit that the end users can test the system (with their own data and emails) prior to the switch over date to ensure everything is in place and databases work correctly.
The system will be completely cloud based and therefore easy for the IT Companies to access. They will be able to purchase the use of the system using CoinDrop or credit card and will only need to purchase what they need, this will allow even small local IT companies the facilities which previously would have been cost prohibitive to them.

Some of the sites we like for reference are -
Lanterbox, brightkits, the sky shifter.

We already have a logo design see attached and the website will need to work with this design.
Please message me if you have any questions
We do have the logo in other file formats if required.
Many Thanks

Target Market(s)

IT Sector

Industry/Entity Type

It Service

Number of Pages Required

5+ page

Requirements
Must have
• Front Page
• About Us
• Contact Info
• Blog
• Benefits
• More Information
• Must be Mobile Phone Compatible/friendly
• Log in (button) and support button on all pages (possibley top right)

```html
<!DOCTYPE html>
<html lang="en">
<head>
<meta charset="utf-8">
<title>Transfer Falcon – Cloud Based Data Migration</title>
<link rel="stylesheet" href="https://fonts.googleapis.com/css2?family=Open+Sans:wght@300;400;600&display=swap">
<style>
:root{
  --brand:#1aa3dc;
  --ink:#2f3338;
  --muted:#8a8f94;
  --light:#b3b7bb;
  --panel:#efefef;
  --dark:#1e222b;
  --white:#ffffff;
  --btn-grey:#5b5d60;
  --footer-grey:#7f8590;
}
*{margin:0;padding:0;box-sizing:border-box}
html,body{width:671px;height:1200px;overflow:hidden}
body{position:relative;font-family:"Open Sans",Arial,sans-serif;color:var(--ink);background:var(--white)}
.abs{position:absolute}
h2,h3,h4{font-weight:400}

/* header */
.site-header{left:0;top:0;width:671px;height:70px;background:var(--white)}
.brand{left:74px;top:14px;display:flex;align-items:center;gap:6px}
.brand-dot{width:14px;height:14px;border-radius:50%;background:var(--brand)}
.brand-name{font-size:13px;font-weight:600;color:var(--ink);letter-spacing:.3px;line-height:1}
.account-btn{top:9px;height:19px;font-size:7px;color:var(--white);display:flex;align-items:center;justify-content:center;border-radius:2px}
.btn-login{left:518px;width:37px;background:var(--brand)}
.btn-support{left:558px;width:37px;background:var(--btn-grey)}
.main-nav{top:44px;left:0;width:671px;font-size:7px;color:var(--muted)}
.main-nav a{position:absolute;color:inherit;text-decoration:none;white-space:nowrap}
.main-nav a.is-active{color:var(--brand)}

/* hero */
.hero{left:0;top:70px;width:671px;height:223px;background:
  radial-gradient(ellipse 90px 60px at 330px 80px,rgba(225,240,250,.9) 0%,rgba(170,215,240,.5) 55%,rgba(170,215,240,0) 100%),
  radial-gradient(ellipse 70px 90px at 300px 190px,rgba(235,170,170,.55) 0%,rgba(235,170,170,0) 100%),
  radial-gradient(ellipse 200px 160px at 150px 100px,rgba(60,190,230,.75) 0%,rgba(60,190,230,0) 100%),
  radial-gradient(ellipse 180px 150px at 560px 80px,rgba(30,110,200,.6) 0%,rgba(30,110,200,0) 100%),
  linear-gradient(90deg,#0a5c8e 0%,#0a3f7a 50%,#061f52 100%)}
.hero-caption{right:74px;top:141px;text-align:right;font-size:14px;line-height:18px;color:var(--white);font-weight:400}
.slider-dots{display:flex;gap:5px;align-items:center;padding:3px 6px;border-radius:8px;background:rgba(0,0,0,.25)}
.slider-dots span{width:5px;height:5px;border-radius:50%;background:var(--white)}
.slider-dots span.is-empty{background:transparent;border:1px solid var(--white)}

/* intro + features */
.intro{left:110px;top:319px;width:451px;text-align:center;font-size:8.5px;line-height:13px;color:var(--muted)}
.feature{top:362px;width:150px;text-align:center}
.feature-icon{width:56px;height:56px;margin:0 auto;border:1px solid var(--brand);border-radius:50%;display:flex;align-items:center;justify-content:center}
.feature-title{margin-top:8px;font-size:13px;color:var(--brand)}
.feature-text{margin-top:4px;font-size:5.4px;line-height:8px;color:var(--muted)}

/* testimonial */
.testimonial-band{left:0;top:501px;width:671px;height:166px;background:
  radial-gradient(ellipse 220px 110px at 470px 70px,rgba(90,90,92,.45) 0%,rgba(90,90,92,0) 100%),
  radial-gradient(ellipse 200px 90px at 250px 140px,rgba(70,78,86,.5) 0%,rgba(70,78,86,0) 100%),
  linear-gradient(120deg,#2b2e31 0%,#1b1d20 60%,#2a2c2f 100%)}
.quote-box{left:74px;top:516px;width:523px;height:90px;border:1px solid #d6d6d6;color:var(--white);font-size:9.3px;line-height:15px;text-align:center;padding:17px 30px 0}
.quote-author{color:var(--brand)}
.quote-badge{left:323px;top:592px;width:26px;height:26px;border-radius:50%;background:var(--brand);border:2px solid var(--white);display:flex;align-items:center;justify-content:center}
.testimonial-dots{left:306px;top:639px;display:flex;gap:13px}
.testimonial-dots span{width:5px;height:5px;border-radius:50%;background:var(--white)}
.testimonial-dots span.is-empty{background:transparent;border:1px solid var(--white)}

/* blog */
.blog-title{left:0;top:691px;width:671px;text-align:center;font-size:27px;font-weight:300;color:var(--ink)}
.post{top:741px;width:161px}
.post-image{width:161px;height:102px}
.post-title{margin-top:10px;font-size:7.3px;line-height:10px;color:var(--ink);font-weight:400}
.post-excerpt{margin-top:7px;font-size:5.3px;line-height:9px;color:var(--light)}
.post-more{margin-top:6px;font-size:5.5px;color:var(--ink);display:flex;align-items:center;gap:3px}
.img-writing{background:
  radial-gradient(ellipse 60px 25px at 70px 45px,rgba(200,30,40,.45) 0%,rgba(200,30,40,0) 100%),
  linear-gradient(135deg,#f3f3f3 0%,#e2e2e2 60%,#d4d4d4 100%)}
.img-team{background:
  radial-gradient(ellipse 50px 35px at 80px 40px,rgba(235,240,245,.9) 0%,rgba(235,240,245,0) 100%),
  radial-gradient(ellipse 40px 30px at 30px 70px,rgba(220,200,40,.45) 0%,rgba(220,200,40,0) 100%),
  radial-gradient(ellipse 40px 30px at 130px 80px,rgba(90,170,60,.45) 0%,rgba(90,170,60,0) 100%),
  linear-gradient(135deg,#c3b59c,#8e8272)}
.img-server{background:
  radial-gradient(ellipse 40px 60px at 40px 55px,rgba(60,120,170,.45) 0%,rgba(60,120,170,0) 100%),
  linear-gradient(90deg,#1f2a33 0%,#2c3a44 50%,#12181d 100%)}

/* map */
.map{left:0;top:970px;width:671px;height:134px;background:
  radial-gradient(ellipse 120px 40px at 500px 80px,rgba(160,200,230,.4) 0%,rgba(160,200,230,0) 100%),
  linear-gradient(180deg,rgba(0,0,0,0) 0%,rgba(0,0,0,0) 75%,rgba(240,170,60,.25) 78%,rgba(0,0,0,0) 82%),
  linear-gradient(180deg,#f1f1ea 0%,#e9ebe2 100%)}
.map-label{left:306px;top:986px;width:60px;height:24px;background:var(--white);font-size:6.5px;color:var(--muted);display:flex;align-items:center;justify-content:center}

/* contact bar */
.contact-bar{left:0;top:1104px;width:671px;height:48px;background:var(--panel)}
.contact-item{top:1124px;display:flex;align-items:center;gap:5px;font-size:6.5px;color:var(--muted)}
.social{left:516px;top:1121px;display:flex;align-items:center;gap:4px}
.social .dot{width:14px;height:14px;border-radius:50%}

/* footer */
.site-footer{left:0;top:1152px;width:671px;height:48px;background:var(--dark)}
.footer-brand{left:72px;top:1163px;width:46px;display:flex;flex-direction:column;align-items:center;gap:3px;font-size:5.5px;color:var(--footer-grey);font-weight:600;white-space:nowrap}
.footer-brand .brand-dot{width:9px;height:9px;background:var(--footer-grey)}
.footer-links{left:129px;top:1163px;font-size:6px;color:var(--white)}
.footer-links span.sep{margin:0 5px;color:#9a9ea6}
.copyright{left:129px;top:1177px;font-size:6px;color:var(--white)}
.to-top{left:577px;top:1166px;width:20px;height:20px;border:1px solid #4e5460;border-radius:50%;display:flex;align-items:center;justify-content:center}
</style>
</head>
<body>

<header class="site-header abs">
  <div class="brand abs"><span class="brand-dot"></span><span class="brand-name">Transfer Falcon</span></div>
  <a class="account-btn btn-login abs">Log in</a>
  <a class="account-btn btn-support abs">Support</a>
  <nav class="main-nav abs">
    <a class="is-active" style="left:406px">Home</a>
    <a style="left:443px">About us</a>
    <a style="left:489px">Benefits</a>
    <a style="left:531px">Blog</a>
    <a style="left:562px">Contact us</a>
  </nav>
</header>

<section class="hero abs" role="img" aria-label="Photo of a finger touching a glowing cloud shape over a blue bokeh background"></section>
<p class="hero-caption abs">Phasellus nisl est,<br>condimentum faucibus</p>
<div class="slider-dots abs" style="left:316px;top:270px"><span class="is-empty"></span><span></span><span></span><span></span></div>

<p class="intro abs">Transfer Falcon is a cloud based migration service providing (to start with) a online migration tool that we migrate Quillnet Relay mailboxes (email) with all the settings, attachments from one system to another.</p>

<div class="feature abs" style="left:74px">
  <div class="feature-icon"><svg width="20" height="14" viewBox="0 0 20 14"><rect x="1" y="1" width="18" height="12" rx="1.5" fill="none" stroke="#1aa3dc" stroke-width="1.3"/><g fill="#1aa3dc"><rect x="4" y="4" width="2" height="1.6"/><rect x="7" y="4" width="2" height="1.6"/><rect x="10" y="4" width="2" height="1.6"/><rect x="13" y="4" width="2" height="1.6"/><rect x="4" y="7" width="2" height="1.6"/><rect x="7" y="7" width="2" height="1.6"/><rect x="10" y="7" width="2" height="1.6"/><rect x="13" y="7" width="2" height="1.6"/><rect x="6" y="10" width="8" height="1.4"/></g></svg></div>
  <h3 class="feature-title">Easy to use</h3>
  <p class="feature-text">Donec vestibulum odio sem, ac laoreet massa ullamcorper id. Donec molestie nisi et tellus hendrerit vehicula. Nunc eu ligula sed quam pulvinar maximus.</p>
</div>
<div class="feature abs" style="left:260px">
  <div class="feature-icon"><svg width="14" height="16" viewBox="0 0 14 16"><path d="M3.5 7V5a3.5 3.5 0 0 1 7 0v2" fill="none" stroke="#1aa3dc" stroke-width="1.8"/><rect x="1.5" y="7" width="11" height="8" rx="1" fill="#1aa3dc"/></svg></div>
  <h3 class="feature-title">Secure</h3>
  <p class="feature-text">Donec vestibulum odio sem, ac laoreet massa ullamcorper id. Donec molestie nisi et tellus hendrerit vehicula. Nunc eu ligula sed quam pulvinar maximus.</p>
</div>
<div class="feature abs" style="left:446px">
  <div class="feature-icon"><svg width="20" height="16" viewBox="0 0 20 16"><path d="M1 1v14h18" fill="none" stroke="#1aa3dc" stroke-width="1.3"/><g fill="#1aa3dc"><rect x="4" y="7" width="2.2" height="7"/><rect x="7.5" y="4" width="2.2" height="10"/><rect x="11" y="8" width="2.2" height="6"/><rect x="14.5" y="5" width="2.2" height="9"/></g></svg></div>
  <h3 class="feature-title">Scalable</h3>
  <p class="feature-text">Donec vestibulum odio sem, ac laoreet massa ullamcorper id. Donec molestie nisi et tellus hendrerit vehicula. Nunc eu ligula sed quam pulvinar maximus.</p>
</div>

<section class="testimonial-band abs" role="img" aria-label="Dark photo of hands working with technology, used as background"></section>
<blockquote class="quote-box abs">“ Phasellus nisl est, condimentum vitae faucibus in, sollicitudin vel metus. Nunc sit amet consequat risus. Curabitur ac elit leo. In eleifend dui tellus, in scelerisque elit porttitor et. Integer eu massa lacinia, lacinia nulla non, volutpat purus. Sed libero felis, vestibulum et dolor eget. ” - &nbsp;<span class="quote-author">Dana Reyes, Company name</span></blockquote>
<div class="quote-badge abs"><svg width="10" height="8" viewBox="0 0 10 8"><path d="M0 8V4.5C0 2 1.3.6 3.6 0l.4.9C2.8 1.4 2.2 2.2 2.2 3.3H4V8zm6 0V4.5C6 2 7.3.6 9.6 0l.4.9C8.8 1.4 8.2 2.2 8.2 3.3H10V8z" fill="#fff"/></svg></div>
<div class="testimonial-dots abs"><span class="is-empty"></span><span></span><span></span><span></span></div>

<h2 class="blog-title abs">Blog</h2>

<article class="post abs" style="left:74px">
  <div class="post-image img-writing" role="img" aria-label="Photo of a hand writing the words data migration"></div>
  <h4 class="post-title">Aenean sed quam non sapien faucibus conse quat vitae sit amet orci.</h4>
  <p class="post-excerpt">Pellentesque blandit lacus eget nunc faucibus, et tincidunt eros viverra. Phasellus consequat sagittis nisi suscipit feugiat. Cras eget leo sed nunc hendrerit ultricies eu at nisl. Praesent iaculis faucibus urna sit amet lacinia.</p>
  <p class="post-more">READ MORE <svg width="4" height="5" viewBox="0 0 4 5"><path d="M0 0l4 2.5L0 5z" fill="#2f3338"/></svg></p>
</article>
<article class="post abs" style="left:254px">
  <div class="post-image img-team" role="img" aria-label="Overhead photo of a team around a table with data charts"></div>
  <h4 class="post-title">Aenean sed quam non sapien faucibus conse quat vitae sit amet orci.</h4>
  <p class="post-excerpt">Pellentesque blandit lacus eget nunc faucibus, et tincidunt eros viverra. Phasellus consequat sagittis nisi suscipit feugiat. Cras eget leo sed nunc hendrerit ultricies eu at nisl. Praesent iaculis faucibus urna sit amet lacinia.</p>
  <p class="post-more">READ MORE <svg width="4" height="5" viewBox="0 0 4 5"><path d="M0 0l4 2.5L0 5z" fill="#2f3338"/></svg></p>
</article>
<article class="post abs" style="left:435px">
  <div class="post-image img-server" role="img" aria-label="Photo of a technician in a server room"></div>
  <h4 class="post-title">Aenean sed quam non sapien faucibus conse quat vitae sit amet orci.</h4>
  <p class="post-excerpt">Pellentesque blandit lacus eget nunc faucibus, et tincidunt eros viverra. Phasellus consequat sagittis nisi suscipit feugiat. Cras eget leo sed nunc hendrerit ultricies eu at nisl. Praesent iaculis faucibus urna sit amet lacinia.</p>
  <p class="post-more">READ MORE <svg width="4" height="5" viewBox="0 0 4 5"><path d="M0 0l4 2.5L0 5z" fill="#2f3338"/></svg></p>
</article>

<section class="map abs" role="img" aria-label="Road map showing the office location"></section>
<div class="map-label abs">Our Location</div>

<section class="contact-bar abs"></section>
<div class="contact-item abs" style="left:74px"><svg width="5" height="7" viewBox="0 0 5 7"><path d="M2.5 0A2.5 2.5 0 0 0 0 2.5C0 4.3 2.5 7 2.5 7S5 4.3 5 2.5A2.5 2.5 0 0 0 2.5 0zm0 3.4a.9.9 0 1 1 0-1.8.9.9 0 0 1 0 1.8z" fill="#8a8f94"/></svg>24 Building name, Streetname, City Zipcode</div>
<div class="contact-item abs" style="left:260px"><svg width="7" height="7" viewBox="0 0 7 7"><path d="M1.4 0l1.2 1.6-.7.9c.4.9 1.1 1.6 2 2l.9-.7L6.4 5 5.6 6.3C2.8 6 .8 4 .5 1.2z" fill="#8a8f94"/></svg>555 010 2437</div>
<div class="contact-item abs" style="left:367px"><svg width="8" height="6" viewBox="0 0 8 6"><rect width="8" height="6" rx=".6" fill="#8a8f94"/><path d="M.4.6L4 3.4 7.6.6" fill="none" stroke="#efefef" stroke-width=".8"/></svg>info@transferfalcon.example</div>
<div class="social abs">
  <svg width="7" height="7" viewBox="0 0 7 7"><g fill="#6b6f74"><circle cx="5.6" cy="1.2" r="1.1"/><circle cx="1.3" cy="3.5" r="1.1"/><circle cx="5.6" cy="5.8" r="1.1"/></g><path d="M5.6 1.2L1.3 3.5l4.3 2.3" fill="none" stroke="#6b6f74" stroke-width=".6"/></svg>
  <span class="dot" style="background:#3b5998"></span>
  <span class="dot" style="background:#1da1f2"></span>
  <span class="dot" style="background:#0077b5"></span>
  <span class="dot" style="background:#e84c3d"></span>
</div>

<footer class="site-footer abs"></footer>
<div class="footer-brand abs"><span class="brand-dot"></span>Transfer Falcon</div>
<div class="footer-links abs">Home<span class="sep">|</span>About us<span class="sep">|</span>Benefits<span class="sep">|</span>Blog<span class="sep">|</span>Contact us</div>
<div class="copyright abs">Copyright © 2016 &nbsp;Transfer Falcon. &nbsp;All rights reserved.</div>
<div class="to-top abs"><svg width="8" height="9" viewBox="0 0 8 9"><path d="M4 9V1M1 4l3-3 3 3" fill="none" stroke="#4e5460" stroke-width="1.2"/></svg></div>

</body>
</html>
```